Bright, Fun and hard to forget home inspection business card.

We need a Business card design for a new Home Inspection company. We are building a brand that is bright, fun and easy to remember.

Target Market(s)

Anyone involed in buying and selling of homes.

Industry/Entity Type

Home Inspection

Contact Information for Business Card

Colin Marlowe Owner/Inspector

Wedsite- PorchAndRafterCheck.example
Phone: 253-555-0187
Email- ColinMarlowe@mailbox.example
WA Lic # 4806

Requirements
Must have
• BRQV LOGO somewhere on card.

```html
<!DOCTYPE html>
<html lang="en">
<head>
<meta charset="utf-8">
<title>Porch &amp; Rafter Check – Business Card</title>
<link rel="stylesheet" href="https://fonts.googleapis.com/css2?family=Tenor+Sans&display=swap">
<style>
  :root {
    --backdrop: #ebebeb;
    --card-white: #f5f5f4;
    --brand-orange: #c6714f;
    --deep-grey: #3c3c3c;
    --panel-grey: #7d7d7d;
    --panel-line: #959595;
    --text-light: #f3f1ef;
    --card-shadow: 0 10px 24px rgba(0,0,0,0.18);
  }
  * { margin: 0; padding: 0; box-sizing: border-box; }
  html, body {
    width: 1200px; height: 720px; overflow: hidden;
    background: var(--backdrop);
    font-family: "Tenor Sans", sans-serif;
  }
  .canvas { position: relative; width: 1200px; height: 720px; }
  .card {
    position: absolute; top: 206px;
    width: 540px; height: 308px;
    overflow: hidden;
    background: var(--card-white);
    box-shadow: var(--card-shadow);
  }
  .card--contact { left: 40px; }
  .card--name { left: 620px; background: var(--brand-orange); }
  .card-shapes { position: absolute; inset: 0; width: 100%; height: 100%; }

  .holder {
    position: absolute; top: 10px; right: 26px;
    text-align: right; color: var(--text-light);
  }
  .holder-name { font-size: 19px; letter-spacing: 3px; text-transform: uppercase; line-height: 26px; }
  .holder-title { font-size: 12px; letter-spacing: 1px; line-height: 16px; }

  .contact-list {
    position: absolute; left: 50px; top: 100px;
    list-style: none; color: var(--text-light);
    font-size: 12px; letter-spacing: 0.4px;
  }
  .contact-list li { height: 38px; line-height: 38px; white-space: nowrap; }

  .brand-mark { position: absolute; display: flex; align-items: center; gap: 8px; }
  .brand-mark .dot {
    width: 22px; height: 22px; border-radius: 50%;
    background: var(--brand-orange); flex: none;
  }
  .brand-mark .brand-name { font-size: 18px; line-height: 1.1; letter-spacing: 0.5px; }
  .card--contact .brand-mark { left: 362px; top: 118px; }
  .card--contact .brand-name { color: var(--brand-orange); }

  .card--name .holder-name {
    position: absolute; left: 110px; top: 96px;
    color: var(--text-light); font-size: 22px; letter-spacing: 4px;
  }
  .card--name .brand-mark { left: 200px; top: 190px; gap: 10px; }
  .card--name .dot { width: 26px; height: 26px; }
  .card--name .brand-name { color: var(--text-light); font-size: 28px; }
</style>
</head>
<body>
<main class="canvas">

  <section class="card card--contact" aria-label="Business card, contact side">
    <svg class="card-shapes" viewBox="0 0 540 308" preserveAspectRatio="none" aria-hidden="true">
      <path fill="var(--brand-orange)" d="M0,0 H540 V60 C450,64 390,72 340,80 C220,84 110,86 0,90 Z"/>
      <path fill="var(--brand-orange)" d="M0,88 H40 C34,170 60,250 120,308 H0 Z"/>
      <path fill="var(--panel-grey)" d="M36,92 C140,88 250,84 340,80 C318,150 330,236 380,308 H120 C60,250 34,170 36,92 Z"/>
      <g stroke="var(--panel-line)" stroke-width="1">
        <line x1="38" y1="138" x2="328" y2="138"/>
        <line x1="40" y1="176" x2="328" y2="176"/>
        <line x1="46" y1="214" x2="334" y2="214"/>
        <line x1="58" y1="252" x2="346" y2="252"/>
      </g>
    </svg>
    <header class="holder">
      <p class="holder-name">Colin Marlowe</p>
      <p class="holder-title">Owner/Inspector</p>
    </header>
    <ul class="contact-list">
      <li>Phone : 253-555-0187</li>
      <li>Email : ColinMarlowe@mailbox.example</li>
      <li>Website : PorchAndRafterCheck.example</li>
      <li>WA Lic # 4806</li>
    </ul>
    <div class="brand-mark">
      <span class="dot"></span>
      <span class="brand-name">Porch &amp; Rafter<br>Check</span>
    </div>
  </section>

  <section class="card card--name" aria-label="Business card, name side">
    <svg class="card-shapes" viewBox="0 0 540 308" preserveAspectRatio="none" aria-hidden="true">
      <path fill="var(--deep-grey)" d="M0,250 C90,210 170,160 270,140 C370,120 460,104 540,96 V308 H0 Z"/>
    </svg>
    <p class="holder-name">Colin Marlowe</p>
    <div class="brand-mark">
      <span class="dot"></span>
      <span class="brand-name">Porch &amp; Rafter<br>Check</span>
    </div>
  </section>

</main>
</body>
</html>
```